Business Card Design to Compliment attached Letterhead

I am looking for a really nice business card for my new business launch. I develop Gridwell based applications to support administrative and operational processes. I have attached my letterhead so you have an idea what the components should look like. I tried uploading the various components into the "Design your own" section, but they looked really rough, so I am looking for someone to be able to come up with a nice crisp version of the tetras square and the Company Name styling that will compliment my letterhead; and then put all of this into a business card design that is crisp, clean and professional looking. I am considering using spot gloss, because I think it will add an extra touch of class.

Industry/Entity Type

Business

Contact Information for Business Card

Kembrin Consulting, Grid Remedies for Routine Snags, Marta Hollowby, Business Systems Analyst, Gridwell Specialist, 0493 058 274, marta@kembrinconsulting.com.au www.kembrinconsulting.com.au

Requirements
Must have
• I want to use the same colors as the attached file and keep the fonts used for "Kembrin" and "Consulting"
• I need the Tetras square to be re-created. I did it myself using photoshop and it is pretty rough. I need it to be crisp and clean and professional looking.
• Please include my name, title, phone, email, web address and "Grid Remedies to Routine Snags"
Nice to have
• So far I have liked the designs that are a little bit different. I want people to look at my card and say "Nice Card"
Should not have
• I don't like the see-through format.
• Do not include any information about Arvel Designs or the address
• Please dont use my version of the tetras square, it is fuzzy and poorly drawn (I did it myself), I need it to be crisp, and clean otherwise it will spoil the effect of my nice new cards.

```html
<!DOCTYPE html>
<html lang="en">
<head>
<meta charset="utf-8">
<title>Kembrin Consulting — Business Card</title>
<link rel="stylesheet" href="https://fonts.googleapis.com/css2?family=Ubuntu:wght@400;500&display=swap">
<style>
  :root {
    --backdrop: #dcdcda;
    --card-white: #ffffff;
    --brand-purple: #5a2f6e;
    --brand-blue: #1a84c4;
    --stripe-light: #2a94d2;
    --stripe-dark: #0f6aa8;
    --band-dark: #3b3c40;
    --band-text: #f2f2f2;
  }
  html, body {
    margin: 0;
    padding: 0;
    width: 1200px;
    height: 1140px;
    overflow: hidden;
    background: var(--backdrop);
    font-family: "Ubuntu", sans-serif;
  }
  .business-card {
    position: absolute;
    left: 75px;
    top: 270px;
    width: 1050px;
    height: 600px;
    background: var(--card-white);
    box-shadow: 0 12px 40px rgba(0,0,0,0.18);
    overflow: hidden;
  }
  .card-bands {
    position: absolute;
    inset: 0;
    width: 100%;
    height: 100%;
  }
  .brand-name {
    position: absolute;
    left: 60px;
    top: 52px;
    margin: 0;
    white-space: nowrap;
    font-weight: 400;
  }
  .brand-name .primary {
    font-size: 92px;
    color: var(--brand-purple);
    font-weight: 500;
    letter-spacing: 1px;
  }
  .brand-name .secondary {
    font-size: 54px;
    color: var(--brand-blue);
    margin-left: 14px;
    font-weight: 500;
  }
  .tagline {
    position: absolute;
    left: 64px;
    top: 176px;
    margin: 0;
    font-size: 25px;
    color: var(--brand-blue);
  }
  .brand-mark {
    position: absolute;
    right: 70px;
    top: 150px;
    display: flex;
    align-items: center;
    gap: 12px;
  }
  .brand-mark .mark-square {
    width: 56px;
    height: 56px;
    background: var(--brand-purple);
  }
  .brand-mark .mark-name {
    font-size: 26px;
    font-weight: 500;
    color: var(--brand-blue);
  }
  .holder-name {
    position: absolute;
    left: 40px;
    top: 400px;
    margin: 0;
    font-size: 44px;
    font-weight: 400;
    letter-spacing: 1px;
    color: var(--band-text);
  }
  .holder-title {
    position: absolute;
    left: 40px;
    top: 458px;
    margin: 0;
    font-size: 24px;
    color: var(--band-text);
  }
  .contact-list {
    position: absolute;
    left: 600px;
    top: 392px;
    margin: 0;
    padding: 0;
    list-style: none;
    font-size: 24px;
    line-height: 38px;
    color: var(--band-text);
  }
  .contact-list .gap { margin-top: 22px; }
</style>
</head>
<body>
  <article class="business-card">
    <svg class="card-bands" viewBox="0 0 1050 600" preserveAspectRatio="none" aria-hidden="true">
      <defs>
        <linearGradient id="stripeGradient" x1="0" y1="0" x2="1" y2="0">
          <stop offset="0" stop-color="#2a94d2"/>
          <stop offset="1" stop-color="#0f6aa8"/>
        </linearGradient>
      </defs>
      <path class="accent-stripe" d="M0,346 Q520,318 1050,222 L1050,600 L0,600 Z" fill="url(#stripeGradient)"/>
      <path class="dark-band" d="M0,370 Q520,344 1050,254 L1050,600 L0,600 Z" fill="#3b3c40"/>
    </svg>

    <h1 class="brand-name"><span class="primary">Kembrin</span><span class="secondary">Consulting</span></h1>
    <p class="tagline">Grid Remedies for Routine Snags</p>

    <div class="brand-mark">
      <span class="mark-square"></span>
      <span class="mark-name">Kembrin</span>
    </div>

    <h2 class="holder-name">MARTA HOLLOWBY</h2>
    <p class="holder-title">Business Systems Analyst, Gridwell Specialist</p>

    <ul class="contact-list">
      <li>+ (000) 0493 058 274</li>
      <li>+ (000) 0493 058 274</li>
      <li class="gap">marta@kembrinconsulting.com.au</li>
      <li>www.kembrinconsulting.com.au</li>
    </ul>
  </article>
</body>
</html>
```